Flyer for the Radiant Harvest Worship Day

I am looking to create a flyer for a one day prayer retreat our church is organizing.
This flyer will be posted on social media, websites and will also be printed so it can be mailed to people.
I am looking for something professional, with good use of our logo and band colors (logo colors).
I am counting on the designer's skill, creativity, art and knowledge of media communication to produce a flyer that will effectively and quickly convey the message we are trying to spread.
CONTENT OF THE FLYER:
Event title: Radiant Harvest Worship Day
Date: Tuesday July 2nd, 2019
Time: 11:00AM - 7:00PM
Belmont Hotel, 4875 Maple Ridge Road, Portland, Maine 04219 (Room: Evergreen)
Event Key words to highlight what the event is about: Prayer, Sharing the Word, Panel discussion, prophecy, Impartation.
Key phrases:
A one day prayer retreat.
Jesus Chris is Lord
Contact info:
www.tuvela.org
Phone: 207 583 2194
Email: contact@brookmeadow.org

```html
<!DOCTYPE html>
<html lang="en">
<head>
<meta charset="utf-8">
<title>Radiant Harvest Worship Day — Flyer</title>
<link rel="stylesheet" href="https://fonts.googleapis.com/css2?family=Allura&family=Jost:wght@400;500;600;700&family=Russo+One&family=Cormorant+Garamond:wght@500&display=swap">
<style>
  :root {
    --page-bg: #5f6077;
    --navy: #0c2547;
    --navy-deep: #08203f;
    --steel: #3f6584;
    --steel-light: #6f93ad;
    --orange: #f39419;
    --white: #ffffff;
    --paper: #eef0f2;
  }
  * { margin: 0; padding: 0; box-sizing: border-box; }
  html, body {
    width: 1200px; height: 800px; overflow: hidden;
    background: var(--page-bg);
  }
  .flyer {
    position: absolute; left: 330px; top: 20px;
    width: 540px; height: 760px;
    background: var(--navy);
    overflow: hidden;
    font-family: "Jost", sans-serif;
    color: var(--white);
  }
  .flyer__photo {
    position: absolute; inset: 0;
    background:
      radial-gradient(ellipse 55% 35% at 30% 30%, rgba(111,147,173,.55), transparent 70%),
      radial-gradient(ellipse 45% 30% at 75% 55%, rgba(63,101,132,.7), transparent 70%),
      radial-gradient(ellipse 60% 30% at 40% 80%, rgba(63,101,132,.6), transparent 70%),
      linear-gradient(160deg, var(--navy-deep) 0%, #1d4468 45%, var(--navy) 100%);
  }
  .brand {
    position: absolute; left: 150px; top: 30px;
    width: 260px; height: 116px;
    background: var(--paper);
    display: flex; align-items: center; justify-content: center; gap: 12px;
  }
  .brand__dot { width: 18px; height: 18px; border-radius: 50%; background: var(--orange); }
  .brand__name {
    font-family: "Cormorant Garamond", serif; font-weight: 500;
    font-size: 54px; color: var(--navy); letter-spacing: 1px;
  }
  .side-label {
    position: absolute; font-size: 11px; letter-spacing: 6px;
    text-transform: uppercase; white-space: nowrap;
    transform-origin: left top; transform: rotate(90deg);
  }
  .side-label--left { left: 62px; top: 130px; }
  .side-label--right { left: 512px; top: 190px; }
  .title {
    position: absolute; right: 66px; top: 160px;
    text-align: right;
    font-family: "Russo One", sans-serif;
    font-size: 52px; line-height: 1; text-transform: uppercase;
    color: transparent;
  }
  .title__line { display: block; -webkit-text-stroke: 2px var(--white); }
  .title__line--accent { -webkit-text-stroke: 2.5px var(--orange); }
  .dots {
    position: absolute; left: 175px; top: 376px;
    display: grid; grid-template-columns: repeat(9, 8px); gap: 8px 12px;
  }
  .dots span { width: 7px; height: 7px; border-radius: 50%; background: var(--white); }
  .tagline {
    position: absolute; left: 0; right: 0; top: 400px;
    text-align: center; line-height: 1.2;
    font-family: "Allura", cursive; font-size: 38px; color: var(--orange);
  }
  .panel-label {
    position: absolute; top: 458px; font-weight: 700; font-size: 15px; line-height: 1;
    letter-spacing: 1px; text-transform: uppercase;
  }
  .panel-label--featuring { left: 128px; }
  .panel-label--date { left: 335px; }
  .box {
    position: absolute; top: 482px; height: 164px;
    border: 2.5px solid var(--orange);
  }
  .box--featuring { left: 118px; width: 160px; padding: 12px 16px; }
  .box--date { left: 300px; width: 160px; padding: 12px 10px; text-align: center; }
  .features { list-style: none; font-weight: 600; font-size: 14px; line-height: 1.1; }
  .features li + li { margin-top: 6px; }
  .date__day { font-size: 19px; font-weight: 500; line-height: 1.3; }
  .date__month { font-size: 20px; font-weight: 700; line-height: 1.3; color: var(--orange); }
  .date__rule { height: 2.5px; background: var(--orange); margin: 8px 0; }
  .date__time { font-size: 22px; font-weight: 700; color: var(--orange); line-height: 1.1; }
  .date__arrow { font-size: 9px; line-height: 1.2; color: var(--orange); }
  .venue {
    position: absolute; left: 0; right: 0; top: 654px; text-align: center;
  }
  .venue__pin { display: block; margin: 0 auto 3px; }
  .venue__address {
    font-weight: 600; font-size: 14px; line-height: 1.25; color: var(--orange);
  }
  .motto {
    position: absolute; left: 0; right: 0; top: 712px; text-align: center;
    font-weight: 700; font-size: 15px; line-height: 1; letter-spacing: 3px;
    text-transform: uppercase; color: var(--orange);
  }
  .contact {
    position: absolute; left: 0; right: 0; top: 734px; text-align: center;
    font-size: 11px; line-height: 1; font-weight: 500; letter-spacing: .5px;
  }
  .footer-strip {
    position: absolute; left: 150px; bottom: 0; width: 240px; height: 8px;
    background: var(--paper);
  }
</style>
</head>
<body>
  <article class="flyer">
    <div class="flyer__photo" role="img" aria-label="Blue-tinted photograph of joined hands held together in prayer over open Bibles"></div>

    <div class="brand">
      <span class="brand__dot"></span>
      <span class="brand__name">Tuvela</span>
    </div>

    <p class="side-label side-label--left">Radiant Harvest Worship Day</p>
    <p class="side-label side-label--right">A One Day Prayer Retreat</p>

    <h1 class="title">
      <span class="title__line title__line--accent">Radiant</span>
      <span class="title__line title__line--accent">Harvest</span>
      <span class="title__line">Worship</span>
      <span class="title__line">Day</span>
    </h1>

    <div class="dots" aria-hidden="true">
      <span></span><span></span><span></span><span></span><span></span><span></span><span></span><span></span><span></span>
      <span></span><span></span><span></span><span></span><span></span><span></span><span></span><span></span><span></span>
    </div>

    <p class="tagline">A One Day Prayer Retreat</p>

    <h2 class="panel-label panel-label--featuring">Featuring</h2>
    <div class="box box--featuring">
      <ul class="features">
        <li>Prayer</li>
        <li>Panel<br>Discussion</li>
        <li>Sharing<br>the word</li>
        <li>Prophecy</li>
        <li>Impartation</li>
      </ul>
    </div>

    <h2 class="panel-label panel-label--date">Date</h2>
    <div class="box box--date">
      <p class="date__day">Tuesday 2nd</p>
      <p class="date__month">JULY, 2019</p>
      <div class="date__rule"></div>
      <p class="date__time">11:00AM</p>
      <p class="date__arrow">▼</p>
      <p class="date__time">7:00PM</p>
    </div>

    <div class="venue">
      <svg class="venue__pin" width="12" height="16" viewBox="0 0 12 16" aria-hidden="true">
        <path d="M6 1a5 5 0 0 0-5 5c0 4 5 9 5 9s5-5 5-9a5 5 0 0 0-5-5z" fill="none" stroke="#fff" stroke-width="1.6"/>
        <circle cx="6" cy="6" r="1.8" fill="#fff"/>
      </svg>
      <p class="venue__address">Belmont Hotel, 4875 Maple Ridge Road, Portland,<br>Maine 04219 (Room: Evergreen)</p>
    </div>

    <p class="motto">Jesus is Lord</p>
    <p class="contact">www.tuvela.org &nbsp;·&nbsp; 207 583 2194 &nbsp;·&nbsp; contact@brookmeadow.org</p>
    <div class="footer-strip"></div>
  </article>
</body>
</html>
```